We are looking for a HTML 5 Responsive Email design for our upcoming concierge services at Prestige Valmorena. We would like this page to be very visual and scream exclusivity and luxury.

We would like the title of the page to say “Take Advantage of Our Concierge Services”
Followed by an image of each of our services:

Luxury Car Hire
Yacht Rental
Private Chef
Dinner on a Yacht Experience
Private Wine Cellar
Airport Transfers
Baby-Sitting Services

Please add at the bottom of the page –
Please get in contact with us at concierge@prestigevalmorena-example.com

I have provided various images of each of some of the services, please choose which you believe are the best fit. (car services is hirequill) On the photo we would like a [Book Now] button.

Overall we would like this to be very visual but still user friendly.

I have attached our logo which should appear on the top left corner, please look at our website for inspiration – www.prestigevalmorena-example.com

Industry/Entity Type

Real Estate

Number of Pages Required

1 page

Font styles to use
Serif

Colors
85acd3
0355a3
ffffff
85cae6
3377b5

Requirements
Must have
• Very visual and eye pleasing. MUST BE A HTML EMAIL.

```html
<!DOCTYPE html>
<html lang="en">
<head>
<meta charset="utf-8">
<title>Prestige Valmorena — Concierge Services</title>
<link href="https://fonts.googleapis.com/css2?family=Jost:wght@400;500;600&display=swap" rel="stylesheet">
<style>
:root{
  --blue:#0355a3;
  --blue-dark:#0d4a8e;
  --blue-mid:#3377b5;
  --sky:#85acd3;
  --text:#6b6b6b;
  --muted:#8a8a8a;
  --band:#f5f5f6;
  --line:#e2e2e2;
  --white:#ffffff;
}
*{box-sizing:border-box;margin:0;padding:0}
html,body{width:1200px;height:2161px;overflow:hidden}
body{font-family:'Jost',sans-serif;color:var(--text);background:var(--white);position:relative}
.abs{position:absolute}
a{color:inherit;text-decoration:none}

/* header */
.site-header{position:absolute;left:0;top:0;width:1200px;height:130px;background:var(--white)}
.brand{position:absolute;left:132px;top:22px;display:flex;align-items:center;gap:12px}
.brand-mark{width:40px;height:40px;background:var(--blue)}
.brand-name{font-size:17px;font-weight:500;color:var(--blue-dark);letter-spacing:1px}
.top-contact{position:absolute;right:132px;top:33px;display:flex;align-items:center;gap:14px;font-size:13px;color:#555;letter-spacing:.3px}
.top-contact .ico{width:24px;height:24px;border-radius:50%;background:var(--blue-dark);display:inline-flex;align-items:center;justify-content:center;margin-right:8px}
.top-contact span{display:inline-flex;align-items:center}
.main-nav{position:absolute;right:132px;top:96px;display:flex;gap:41px;font-size:11.5px;letter-spacing:.8px;color:#777}
.main-nav .active{color:var(--blue)}

/* hero */
.hero{position:absolute;left:0;top:130px;width:1200px;height:461px;background:linear-gradient(100deg,#4d4a45 0%,#8a8378 25%,#d8cfc2 45%,#b9b5ae 70%,#8c98a1 100%)}
.hero-panel{position:absolute;left:0;top:145px;width:468px;height:216px;background:rgba(80,80,80,.72)}
.hero-title{position:absolute;left:132px;top:160px;font-size:49px;font-weight:500;color:var(--white);letter-spacing:1.5px}
.hero-text{position:absolute;left:133px;top:228px;width:320px;font-size:11px;line-height:19px;color:#eee}
.btn{display:inline-flex;align-items:center;justify-content:center;background:var(--blue);color:var(--white);border-radius:2px}
.hero-btn{position:absolute;left:134px;top:291px;width:137px;height:45px;font-size:15px;letter-spacing:.5px;font-weight:500}
.hero-next{position:absolute;left:1096px;top:219px;width:32px;height:32px;border-radius:50%;background:rgba(120,120,120,.8);display:flex;align-items:center;justify-content:center}

/* section headings */
.section-title{position:absolute;left:0;width:1200px;text-align:center;color:var(--blue-dark);font-weight:500;letter-spacing:1.5px}
.lead{position:absolute;left:330px;width:540px;text-align:center;font-size:11px;line-height:23px;color:var(--text)}

/* features */
.feature{position:absolute;top:760px;width:260px;text-align:center}
.feature svg{display:block;margin:0 auto}
.feature h3{margin-top:16px;font-size:19px;font-weight:500;color:var(--blue-dark);letter-spacing:1px}
.feature p{margin-top:18px;font-size:10.5px;line-height:24px;text-align:justify;text-align-last:center;color:var(--text)}

/* services */
.services{position:absolute;left:0;top:981px;width:1200px;height:521px;background:var(--band)}
.service{position:absolute;top:130px;width:294px}
.service-photo{width:294px;height:151px;border:4px solid var(--white);box-shadow:0 0 0 1px var(--line)}
.service h3{margin-top:22px;font-size:19px;font-weight:500;color:var(--blue-dark);letter-spacing:1px}
.service p{margin-top:10px;font-size:10.5px;line-height:24px;color:var(--text)}
.service .btn{margin-top:20px;width:97px;height:33px;font-size:12.5px;letter-spacing:.3px}
.slide-arrow{position:absolute;top:266px}

/* news */
.news-item{position:absolute;top:1639px;width:450px;height:150px}
.news-photo{position:absolute;left:0;top:0;width:167px;height:149px;border:4px solid var(--white);box-shadow:0 0 0 1px var(--line)}
.news-body{position:absolute;left:195px;top:0;width:254px}
.news-date{font-size:10.5px;color:#666}
.news-body h3{margin-top:6px;font-size:19px;font-weight:500;color:var(--blue-dark);letter-spacing:1px}
.news-body p{margin-top:4px;font-size:10.5px;line-height:24px;text-align:justify;color:var(--text)}
.read-more{font-size:10.5px;color:var(--blue)}

/* footer */
.site-footer{position:absolute;left:0;top:1847px;width:1200px;height:314px;background:var(--band)}
.footer-brand{position:absolute;left:132px;top:70px;display:flex;align-items:center;gap:12px}
.footer-col{position:absolute;top:44px}
.footer-col h4{font-size:14.5px;font-weight:500;color:var(--blue-dark);letter-spacing:.3px}
.sitemap li{list-style:none;font-size:10px;line-height:24px;color:#666}
.sitemap ul{margin-top:14px}
.newsletter p{margin-top:18px;width:260px;font-size:10px;line-height:24px;color:#666}
.mail-input{margin-top:18px;width:251px;height:42px;border:1px solid #ddd;border-radius:3px;background:var(--white);font-size:10.5px;color:#555;padding:14px 14px}
.subscribe{margin-top:20px;width:81px;height:29px;font-size:9.5px;letter-spacing:.8px}
.contact-list{margin-top:14px;list-style:none}
.contact-list li{display:flex;align-items:flex-start;gap:12px;font-size:10px;line-height:14px;color:#666;margin-bottom:13px}
.contact-list svg{flex:none;margin-top:1px}
.contact-list .email{text-decoration:underline}
.footer-rule{position:absolute;left:132px;top:249px;width:936px;height:1px;background:#d6d6d6}
.copyright{position:absolute;left:132px;top:278px;font-size:10px;color:#888}
.social{position:absolute;right:132px;top:276px;display:flex;gap:22px}
.social span{width:14px;height:14px;border-radius:50%;background:#555;display:block}
</style>
</head>
<body>

<header class="site-header">
  <div class="brand">
    <span class="brand-mark"></span>
    <span class="brand-name">PRESTIGE VALMORENA</span>
  </div>
  <div class="top-contact">
    <span><i class="ico"><svg width="12" height="12" viewBox="0 0 24 24"><path fill="#fff" d="M6.6 10.8a15 15 0 0 0 6.6 6.6l2.2-2.2c.3-.3.7-.4 1-.2 1.1.4 2.3.6 3.6.6.6 0 1 .4 1 1V20c0 .6-.4 1-1 1A17 17 0 0 1 3 4c0-.6.4-1 1-1h3.5c.6 0 1 .4 1 1 0 1.3.2 2.5.6 3.6.1.3 0 .7-.2 1z"/></svg></i>+34 900 555 014</span>
    <span><i class="ico"><svg width="12" height="12" viewBox="0 0 24 24"><path fill="#fff" d="M2 5h20v14H2z"/><path d="M2 5l10 8 10-8" fill="none" stroke="#0d4a8e" stroke-width="2"/></svg></i>concierge@prestigevalmorena-example.com</span>
  </div>
  <nav class="main-nav">
    <a class="active">HOME</a><a>ABOUT US</a><a>SERVICES</a><a>FEATURES</a><a>NEWS</a><a>CONTACT US</a>
  </nav>
</header>

<section class="hero" role="img" aria-label="Guests relaxing on the deck of a sailing yacht in the sun">
  <div class="hero-panel"></div>
  <h1 class="hero-title">Yacht Rental</h1>
  <p class="hero-text">Nemo enim ipsam voluptatem quia voluptas sit aspernatur aut odit aut fugit, sed quia consequuntur magni</p>
  <a class="btn hero-btn">BOOK NOW</a>
  <span class="hero-next"><svg width="12" height="14" viewBox="0 0 12 14"><path d="M3 1l6 6-6 6" fill="none" stroke="#fff" stroke-width="2"/></svg></span>
</section>

<h2 class="section-title" style="top:626px;font-size:29px">Welcome to Prestige Valmorena</h2>
<p class="lead" style="top:682px">Nemo enim ipsam voluptatem quia voluptas sit aspernatur aut odit aut fugit, sed quia consequuntur magni dolores eos qui ratione voluptatem sequi nesciunt.</p>

<div class="feature" style="left:132px">
  <svg width="40" height="36" viewBox="0 0 40 36"><path d="M4 4h24v14a8 8 0 0 1-8 8h-8a8 8 0 0 1-8-8z" fill="#777"/><path d="M28 8h4a4 4 0 0 1 0 8h-4" fill="none" stroke="#777" stroke-width="3"/><rect x="0" y="30" width="34" height="4" fill="#777"/></svg>
  <h3>Exclusivity</h3>
  <p>Nemo enim ipsam voluptatem quia voluptas sit aspernatur aut odit aut fugit, sed quia consequuntur magni dolores eos qui ratione</p>
</div>
<div class="feature" style="left:469px">
  <svg width="36" height="38" viewBox="0 0 36 38"><path d="M1 1h34L20 18v14h-4V18z" fill="#777"/><rect x="8" y="33" width="20" height="4" fill="#777"/></svg>
  <h3>Luxury</h3>
  <p>Nemo enim ipsam voluptatem quia voluptas sit aspernatur aut odit aut fugit, sed quia consequuntur magni dolores eos qui ratione</p>
</div>
<div class="feature" style="left:806px">
  <svg width="34" height="40" viewBox="0 0 34 40"><path d="M2 1v12a5 5 0 0 0 4 5v21h4V18a5 5 0 0 0 4-5V1h-2.5v10h-2V1H7v10H5V1z" fill="#777"/><path d="M22 1c6 0 10 6 10 16h-4v22h-6z" fill="#777"/></svg>
  <h3>Dinner</h3>
  <p>Nemo enim ipsam voluptatem quia voluptas sit aspernatur aut odit aut fugit, sed quia consequuntur magni dolores eos qui ratione</p>
</div>

<section class="services">
  <h2 class="section-title" style="top:60px;font-size:30px">Take Advantage of Our Concierge Services</h2>
  <svg class="slide-arrow" style="left:80px" width="12" height="24" viewBox="0 0 12 24"><path d="M11 1L1 12l10 11" fill="none" stroke="#555" stroke-width="1.5"/></svg>
  <svg class="slide-arrow" style="left:1097px" width="12" height="24" viewBox="0 0 12 24"><path d="M1 1l10 11L1 23" fill="none" stroke="#555" stroke-width="1.5"/></svg>

  <article class="service" style="left:131px">
    <div class="service-photo" role="img" aria-label="Yellow sports car parked on a coastal road" style="background:linear-gradient(160deg,#6b5a3a,#c9c24a 45%,#e6e03a 60%,#4a4030)"></div>
    <h3>Luxury Car Hire</h3>
    <p>Nemo enim ipsam voluptatem quia voluptas sit aspernatur aut odit aut fugit, sed quia consequuntur magni dolores eos qui ratione voluptatem sequi nesciunt.</p>
    <a class="btn">View Details</a>
  </article>
  <article class="service" style="left:454px">
    <div class="service-photo" role="img" aria-label="White motor yacht cruising on deep blue water" style="background:linear-gradient(180deg,#9fb6cc 0%,#6f8aa4 35%,#e9eef2 55%,#1f4a7a 70%,#0f3560 100%)"></div>
    <h3>Yacht Rental</h3>
    <p>Nemo enim ipsam voluptatem quia voluptas sit aspernatur aut odit aut fugit, sed quia consequuntur magni dolores eos qui ratione voluptatem sequi nesciunt.</p>
    <a class="btn">View Details</a>
  </article>
  <article class="service" style="left:774px">
    <div class="service-photo" role="img" aria-label="Private chef plating a garnished dish" style="background:linear-gradient(120deg,#eae7e2,#d9c2ae 45%,#f3f1ee 70%,#c9c4bd)"></div>
    <h3>Private Chef</h3>
    <p>Nemo enim ipsam voluptatem quia voluptas sit aspernatur aut odit aut fugit, sed quia consequuntur magni dolores eos qui ratione voluptatem sequi nesciunt.</p>
    <a class="btn">View Details</a>
  </article>
</section>

<h2 class="section-title" style="top:1555px;font-size:30px">Recent News</h2>

<article class="news-item" style="left:131px">
  <div class="news-photo" role="img" aria-label="Wine bottles stacked in a cellar rack" style="background:linear-gradient(135deg,#3a1c0e,#8a4a22 40%,#c58a4a 55%,#4a2412)"></div>
  <div class="news-body">
    <div class="news-date">Mar 04,2017</div>
    <h3>Concierge</h3>
    <p>Nemo enim ipsam voluptatem quia voluptas sit aspernatur aut odit aut fugit, sed quia consequuntur magni dolores eos qui ratione</p>
    <a class="read-more">Read More</a>
  </div>
</article>
<article class="news-item" style="left:621px">
  <div class="news-photo" role="img" aria-label="Rows of wine bottles lying in a rack" style="background:linear-gradient(135deg,#2a160c,#6a3a1c 40%,#d8c2a0 55%,#3a2012)"></div>
  <div class="news-body">
    <div class="news-date">Mar 04,2017</div>
    <h3>Concierge</h3>
    <p>Nemo enim ipsam voluptatem quia voluptas sit aspernatur aut odit aut fugit, sed quia consequuntur magni dolores eos qui ratione</p>
    <a class="read-more">Read More</a>
  </div>
</article>

<footer class="site-footer">
  <div class="footer-brand">
    <span class="brand-mark"></span>
    <span class="brand-name">PRESTIGE VALMORENA</span>
  </div>

  <div class="footer-col sitemap" style="left:395px">
    <h4>Sitemap</h4>
    <ul><li>Home</li><li>About us</li><li>Services</li><li>Features</li><li>News</li><li>Contact us</li></ul>
  </div>

  <div class="footer-col newsletter" style="left:597px">
    <h4>Newsletter</h4>
    <p>Enter your email address to receive the latest news and notes from our blog.</p>
    <div class="mail-input">Enter Your Mail Id</div>
    <a class="btn subscribe">SUBSCRIBE</a>
  </div>

  <div class="footer-col" style="left:889px">
    <h4>Contact us</h4>
    <ul class="contact-list">
      <li><svg width="12" height="12" viewBox="0 0 24 24"><path fill="#666" d="M6.6 10.8a15 15 0 0 0 6.6 6.6l2.2-2.2c.3-.3.7-.4 1-.2 1.1.4 2.3.6 3.6.6.6 0 1 .4 1 1V20c0 .6-.4 1-1 1A17 17 0 0 1 3 4c0-.6.4-1 1-1h3.5c.6 0 1 .4 1 1 0 1.3.2 2.5.6 3.6.1.3 0 .7-.2 1z"/></svg>(555) 014-2200</li>
      <li><svg width="12" height="12" viewBox="0 0 24 24"><rect x="6" y="2" width="12" height="6" fill="#666"/><rect x="2" y="9" width="20" height="9" fill="#666"/><rect x="6" y="15" width="12" height="7" fill="#666" stroke="#f5f5f6" stroke-width="1.5"/></svg>(555) 014-2200</li>
      <li><svg width="12" height="12" viewBox="0 0 24 24"><path fill="#666" d="M2 5h20v14H2z"/><path d="M2 5l10 8 10-8" fill="none" stroke="#f5f5f6" stroke-width="2"/></svg><span class="email">concierge@prestigevalmorena-example.com</span></li>
      <li><svg width="12" height="14" viewBox="0 0 24 28"><path fill="#666" d="M12 0a9 9 0 0 0-9 9c0 7 9 19 9 19s9-12 9-19a9 9 0 0 0-9-9zm0 12a3 3 0 1 1 0-6 3 3 0 0 1 0 6z"/></svg><span>#2868 Lorem ipsum dolor sit<br>amet, consectetur</span></li>
    </ul>
  </div>

  <div class="footer-rule"></div>
  <p class="copyright">©2017 prestigevalmorena-example.com. All Rights Reserved.</p>
  <div class="social" aria-label="Social links"><span></span><span></span><span></span><span></span></div>
</footer>

</body>
</html>
```